Web Design for an Online Dating Web Site

We need an uncoded web design for a new online dating web site called zMatchy.net. Simplicity and boldness are the key factors in the successful design.
Please look at the requirements document attached for details.
Updates
Dear all,
Please AVOID USING A PICTURE OF A HAPPY COUPLE ON THE HOME PAGE of the site. We highly want to move away from this space as it makes our web site just like another dating web site.
We like something simple with web 2.0 look and feel. The examples in the Requirements Document are exactly the design we are after.
Regards
Tarn
Industry/Entity Type
Dating
Look and feel
Each slider illustrates characteristics of the customer's brand and the style your logo design should communicate.

```html
<!DOCTYPE html>
<html lang="en">
<head>
<meta charset="utf-8">
<title>zMatchy.net – My Messages</title>
<link rel="stylesheet" href="https://fonts.googleapis.com/css2?family=Arimo:wght@400;700&family=Open+Sans:wght@400;600&display=swap">
<style>
:root{
  --green:#8cc84f;
  --green-light:#bfe382;
  --green-btn:#9bd160;
  --green-field:#7a9a4e;
  --green-area:#80a557;
  --grey-btn:#b9b9b9;
  --panel:#ebebeb;
  --panel-sel:#cdcdcd;
  --text:#555;
  --text-soft:#999;
  --white:#fff;
  --footer:#0a0a0a;
  --footer-band:#1b1b1b;
  --footer-text:#5e5e5e;
  --logo:#6d6d6d;
}
*{box-sizing:border-box;margin:0;padding:0}
html,body{width:1200px;height:1109px;overflow:hidden}
body{position:relative;font-family:"Open Sans",Verdana,sans-serif;color:var(--text);background:var(--white)}
.abs{position:absolute}

/* header */
.site-header{position:absolute;left:0;top:0;width:1200px;height:131px;background:linear-gradient(#fff,#f3f3f3);border-bottom:2px solid #cfcfcf}
.brand{position:absolute;left:147px;top:12px;display:flex;align-items:center;gap:12px}
.brand-name{font-family:"Arimo",sans-serif;font-weight:700;font-size:54px;color:var(--logo);letter-spacing:-1px}
.brand-dot{width:22px;height:22px;border-radius:50%;background:var(--green)}
.main-nav{position:absolute;top:20px;left:620px;display:flex;gap:9px}
.nav-btn{height:31px;padding:0 14px;border-radius:9px;background:linear-gradient(#cacaca,#adadad);color:#fff;font-family:"Arimo",sans-serif;font-size:15px;line-height:31px}
.nav-btn.is-active{background:linear-gradient(#acdc76,#8cc84f)}
.stuff-panel{position:absolute;left:645px;top:59px;width:348px;height:64px;background:#e3e3e3;border-radius:8px;text-align:center}
.stuff-title{font-family:"Arimo",sans-serif;font-size:18px;color:#555;margin-top:4px}
.stuff-title span{font-size:10px;vertical-align:middle}
.stuff-links{position:absolute;left:35px;top:30px;font-size:11px;line-height:12px;color:#666;display:grid;grid-template-columns:78px 78px auto;text-align:left}

/* stage */
.stage{position:absolute;left:0;top:131px;width:1200px;height:677px;background:radial-gradient(ellipse 480px 360px at 850px 260px,var(--green-light),var(--green) 90%)}
.page-title{position:absolute;left:190px;top:50px;width:190px;height:37px;background:linear-gradient(90deg,rgba(255,255,255,.2),rgba(255,255,255,0));padding-left:26px;color:#fff;font-size:20px;line-height:37px}
.msg-list{position:absolute;left:186px;top:93px;width:310px;height:503px;background:var(--panel);border-radius:8px;box-shadow:0 1px 3px rgba(0,0,0,.25);padding-top:12px}
.msg-row{position:relative;height:97px;border-bottom:1px solid #d8d8d8}
.msg-row.is-selected{background:var(--panel-sel)}
.avatar{position:absolute;left:32px;top:7px;width:66px;height:66px;border:2px solid #fff;box-shadow:0 1px 3px rgba(0,0,0,.35)}
.photo-couple{background:linear-gradient(135deg,#6f8f3a,#a4476e 55%,#7b6a55)}
.photo-pair{background:linear-gradient(135deg,#3c3b36,#a58a74 60%,#4b4038)}
.icon-female{background:linear-gradient(#f2f2f2,#e6a0d8)}
.icon-male{background:linear-gradient(#f2f2f2,#69aee0)}
.member{position:absolute;left:0;width:130px;top:77px;text-align:center;font-size:13px;color:#555}
.msg-meta{position:absolute;left:112px;top:14px;width:195px;font-size:13px}
.msg-line{display:flex;height:23px;line-height:23px}
.msg-line dt{width:67px;text-align:right;color:#444;padding-right:9px}
.msg-line dd{flex:1;color:#555;border-bottom:1px solid #d8d8d8;padding-left:3px}
.msg-date{position:absolute;left:113px;top:62px;font-size:10px;color:var(--text-soft);letter-spacing:1px}
.pager-arrow{position:absolute;top:190px;width:70px;height:71px;background:linear-gradient(#f7f7f7,#d5d5d5);box-shadow:0 4px 4px rgba(0,0,0,.4)}
.pager-arrow.prev{left:0;border-radius:0 8px 8px 0}
.pager-arrow.next{left:1130px;border-radius:8px 0 0 8px}
.pager-arrow svg{position:absolute;left:17px;top:15px}

.detail-photo{position:absolute;left:540px;top:111px;width:146px;height:133px;border:2px solid #fff;box-shadow:0 1px 4px rgba(0,0,0,.3)}
.sender-band{position:absolute;left:686px;top:146px;width:170px;height:51px;background:linear-gradient(90deg,rgba(255,255,255,.25),rgba(255,255,255,0));padding-left:8px}
.sender-name{color:#fff;font-size:18px;margin-top:6px}
.sender-date{font-size:10px;color:#4a5e33;letter-spacing:1px;margin-top:-3px}
.field-label{position:absolute;left:540px;color:#fff;font-size:17px}
.subject-field{position:absolute;left:540px;top:285px;width:478px;height:31px;background:var(--green-field);color:#fff;font-size:13px;line-height:31px;padding-left:11px}
.toolbar{position:absolute;left:540px;top:356px;width:478px;height:32px;background:linear-gradient(#f5f5f5,#dcdcdc);display:flex;align-items:center;gap:8px;padding-left:23px}
.tool{height:22px;min-width:22px;border:1px solid #c5c5c5;border-radius:3px;background:#fafafa;font-size:11px;color:#222;display:flex;align-items:center;justify-content:center;font-family:"Arimo",sans-serif;padding:0 4px}
.tool.font-pick{width:84px}
.tool.size-pick{width:32px;margin-right:4px}
.response-area{position:absolute;left:540px;top:388px;width:478px;height:188px;background:var(--green-area);color:#eef5e4;font-size:13px;padding:4px 11px}
.slide-dots{position:absolute;left:548px;top:634px;display:flex;gap:17px}
.slide-dots i{width:13px;height:13px;border-radius:50%;background:#7fae4d}
.slide-dots i.is-current{background:#f2f2f2}

/* footer */
.site-footer{position:absolute;left:0;top:808px;width:1200px;height:301px;background:var(--footer)}
.footer-band{height:25px;background:var(--footer-band)}
.footer-head{position:absolute;top:4px;color:#fff;font-family:"Arimo",sans-serif;font-size:13px}
.footer-links{position:absolute;left:247px;top:34px;font-size:11px;line-height:16px;color:var(--footer-text);list-style:none}
.input{position:absolute;left:419px;width:124px;height:23px;background:#333;border-radius:4px;color:#666;font-size:10px;padding:5px 10px}
.send-btn{position:absolute;left:419px;top:217px;width:67px;height:22px;background:#222;border-radius:3px;color:#fff;font-size:13px;text-align:center;line-height:22px}
.social{position:absolute;left:650px;top:38px;display:flex;gap:8px}
.social i{width:22px;height:22px;border-radius:3px;display:block}
.badge{position:absolute;border-radius:3px;background:#f0f0f0}
.count{position:absolute;font-size:11px;color:#777}
.contact{position:absolute;left:847px;top:34px;font-size:11px;line-height:16px;color:var(--footer-text)}
.contact b{color:#ccc;font-weight:400}
.footer-brand{position:absolute;left:850px;top:90px;display:flex;align-items:center;gap:8px}
.footer-brand span{font-family:"Arimo",sans-serif;font-weight:700;font-size:30px;color:#777}
.footer-brand i{width:12px;height:12px;border-radius:50%;background:#777}
.legal{position:absolute;top:268px;width:1200px;text-align:center;font-size:9px;line-height:14px;color:#666}
</style>
</head>
<body>
<header class="site-header">
  <div class="brand"><span class="brand-name">zMatchy</span><i class="brand-dot"></i></div>
  <nav class="main-nav">
    <span class="nav-btn is-active">my messages</span>
    <span class="nav-btn">start dating</span>
    <span class="nav-btn">sign out</span>
    <span class="nav-btn">help</span>
  </nav>
  <div class="stuff-panel">
    <div class="stuff-title">my stuff <span>▼</span></div>
    <div class="stuff-links"><span>My Details</span><span>My Friends</span><span>My Seeking Criteria</span><span>My Avatar</span><span>My Video</span></div>
  </div>
</header>

<main class="stage">
  <h1 class="page-title">My Messages</h1>
  <section class="msg-list">
    <article class="msg-row is-selected">
      <div class="avatar photo-couple" role="img" aria-label="Profile photo of Lena"></div>
      <div class="member" style="top:79px">Lena</div>
      <dl class="msg-meta"><div class="msg-line"><dt>Subject:</dt><dd>Whats up cut...</dd></div><div class="msg-line"><dt>Message:</dt><dd>You should te...</dd></div></dl>
      <div class="msg-date">10/05/2011</div>
    </article>
    <article class="msg-row">
      <div class="avatar photo-pair" role="img" aria-label="Profile photo of Mara"></div>
      <div class="member">Mara</div>
      <dl class="msg-meta"><div class="msg-line"><dt>Subject:</dt><dd>I'm new here...</dd></div><div class="msg-line"><dt>Message:</dt><dd>I want to set...</dd></div></dl>
      <div class="msg-date">10/03/2011</div>
    </article>
    <article class="msg-row">
      <div class="avatar icon-female" role="img" aria-label="Default female avatar for Ivy"></div>
      <div class="member">Ivy</div>
      <dl class="msg-meta"><div class="msg-line"><dt>Subject:</dt><dd>I'm new here...</dd></div><div class="msg-line"><dt>Message:</dt><dd>I want to set...</dd></div></dl>
      <div class="msg-date">09/27/2011</div>
    </article>
    <article class="msg-row">
      <div class="avatar icon-male" role="img" aria-label="Default male avatar for Owen"></div>
      <div class="member">Owen</div>
      <dl class="msg-meta"><div class="msg-line"><dt>Subject:</dt><dd>I'm new here...</dd></div><div class="msg-line"><dt>Message:</dt><dd>I want to set...</dd></div></dl>
      <div class="msg-date">09/23/2011</div>
    </article>
    <article class="msg-row" style="border-bottom:0">
      <div class="avatar photo-couple" role="img" aria-label="Profile photo of Lena"></div>
      <div class="member">Lena</div>
      <dl class="msg-meta"><div class="msg-line"><dt>Subject:</dt><dd>I'm new here...</dd></div><div class="msg-line"><dt>Message:</dt><dd>I want to set...</dd></div></dl>
      <div class="msg-date">09/15/2011</div>
    </article>
  </section>

  <a class="pager-arrow prev" aria-label="Previous"><svg width="36" height="42"><polyline points="30,3 8,21 30,39" fill="none" stroke="#b4b4b4" stroke-width="6"/></svg></a>
  <a class="pager-arrow next" aria-label="Next"><svg width="36" height="42"><polyline points="8,3 30,21 8,39" fill="none" stroke="#b4b4b4" stroke-width="6"/></svg></a>

  <div class="detail-photo photo-couple" role="img" aria-label="Profile photo of Lena Hart"></div>
  <div class="sender-band"><div class="sender-name">Lena Hart</div><div class="sender-date">10/05/2011</div></div>
  <div class="field-label" style="top:260px">Subject</div>
  <div class="subject-field">RE: Whats up cutie? Let's Talk</div>
  <div class="field-label" style="top:326px">Enter Response</div>
  <div class="toolbar">
    <span class="tool font-pick">Verdana ▾</span>
    <span class="tool size-pick">12▾</span>
    <span class="tool"><b>B</b></span>
    <span class="tool"><i>I</i></span>
    <span class="tool"><u>U</u></span>
    <span class="tool" style="font-size:8px"><s>ABC</s></span>
    <span class="tool"><svg width="12" height="10"><path d="M0 1h12M0 4h8M0 7h12M0 10h8" stroke="#333"/></svg></span>
    <span class="tool"><svg width="12" height="10"><path d="M0 1h12M2 4h8M0 7h12M2 10h8" stroke="#333"/></svg></span>
    <span class="tool"><svg width="12" height="10"><path d="M0 1h12M4 4h8M0 7h12M4 10h8" stroke="#333"/></svg></span>
    <span class="tool"><svg width="10" height="10"><rect width="4" height="4" fill="#e55"/><rect x="6" width="4" height="4" fill="#5a5"/><rect y="6" width="4" height="4" fill="#55e"/><rect x="6" y="6" width="4" height="4" fill="#ec4"/></svg></span>
    <span class="tool"><svg width="14" height="14"><circle cx="7" cy="7" r="6.5" fill="#444"/></svg></span>
    <span class="tool">Σ</span>
  </div>
  <div class="response-area">Enter response here...</div>
  <div class="slide-dots"><i class="is-current"></i><i></i><i></i><i></i><i></i></div>
</main>

<footer class="site-footer">
  <div class="footer-band"></div>
  <h2 class="footer-head" style="left:248px">Read More</h2>
  <h2 class="footer-head" style="left:422px">Let's Talk</h2>
  <h2 class="footer-head" style="left:650px">Get Social</h2>
  <h2 class="footer-head" style="left:848px">Contact Us</h2>
  <ul class="footer-links"><li>Why zMatchy?</li><li>How It Works</li><li>Sign Up</li><li>Login</li><li>About Us</li></ul>
  <div class="input" style="top:37px">name</div>
  <div class="input" style="top:67px">email address</div>
  <div class="input" style="top:97px;width:181px;height:114px">type message here...</div>
  <div class="send-btn">Send</div>
  <div class="social"><i style="background:#3b5a9a"></i><i style="background:#e5761e"></i><i style="background:#3a9ad0"></i><i style="background:#2e8a4a"></i></div>
  <div class="badge" style="left:650px;top:69px;width:38px;height:22px"></div>
  <div class="badge" style="left:693px;top:69px;width:38px;height:22px;background:#fff"></div>
  <span class="count" style="left:701px;top:73px;color:#555">1.4k</span>
  <div class="badge" style="left:650px;top:100px;width:48px;height:24px"></div>
  <span class="count" style="left:706px;top:105px;width:11px;height:11px;background:#3b5a9a;border-radius:2px"></span>
  <span class="count" style="left:721px;top:104px;color:#555">3,400 Likes</span>
  <address class="contact" style="font-style:normal">18 Orchard Lane<br>54321, Ohio<br><b>1.800.555.0142</b></address>
  <div class="footer-brand"><span>zMatchy</span><i></i></div>
  <div class="legal">© 2011 zMatchy.net<br>zMatchy #1 Trusted Relationship Site - Know Your Match</div>
</footer>
</body>
</html>
```